Jewish & Muslim Interfaith Dialogue titled "We Walk Beside" by US Non-Profit Velmora.Foundation

Residences through the USA strive for cooperative democracy within the United States of America's neighborhoods. We are for peaceful collaborations within the Western views and Muslim. We discuss the practice existence in modern society of Shariah Law in a cooperation and neighborly conservation between Muslim Imam Tarek Holloun and Dennis Palfrey a Jewish retired US federal prosecutor.

Our website is currently under redesign but the logo for the foundation is current at velmora.foundation view Imam Tarek's bio at itarekh.com

Target Market(s)

Any interested in Interfaith, Islam and Peaceful Democracy

Industry/Entity Type

Interfaith religious democratic america

Font styles to use
Sans Serif
Decorative

Requirements
Must have
• Use also some color scheme to compliment logo. Some elements from the drafted design in visuals for the worlds that are written around the book title
Nice to have
• The velmora logo and other people.
Should not have
• Any violent images

```html
<!DOCTYPE html>
<html lang="en">
<head>
<meta charset="utf-8">
<title>We Walk Beside — Jewish &amp; Muslim Interfaith Dialogue</title>
<link rel="stylesheet" href="https://fonts.googleapis.com/css2?family=Italiana&family=Roboto+Condensed:wght@400;500&display=swap">
<style>
  :root {
    --page-bg: #ffffff;
    --sky-top: #5f9fd6;
    --sky-mid: #bcd8ee;
    --horizon: #e9eef0;
    --trees: #7d9a62;
    --water-top: #8fbbdc;
    --water-bottom: #4c8cc8;
    --title-ink: #3b4838;
    --title-edge: #f4f7f2;
    --subtitle-ink: #1f2a33;
    --keyword-ink: #e6f3c9;
    --byline-ink: #ffffff;
    --symbol-ink: rgba(255, 255, 255, 0.55);
  }
  * { box-sizing: border-box; margin: 0; padding: 0; }
  html, body {
    width: 1200px;
    height: 1106px;
    overflow: hidden;
    background: var(--page-bg);
  }
  .cover {
    position: absolute;
    left: 320px;
    top: 33px;
    width: 560px;
    height: 1040px;
    overflow: hidden;
    font-family: "Roboto Condensed", sans-serif;
  }
  .cover-art {
    position: absolute;
    inset: 0;
    background:
      linear-gradient(180deg,
        var(--sky-top) 0%,
        var(--sky-mid) 28%,
        var(--horizon) 48%,
        var(--trees) 58%,
        var(--horizon) 60%,
        var(--water-top) 64%,
        var(--water-bottom) 100%);
  }
  .title {
    position: absolute;
    left: 20px;
    width: 460px;
    top: 96px;
    text-align: center;
    font-family: "Italiana", serif;
    font-weight: 400;
    color: var(--title-ink);
    text-shadow: 0 0 2px var(--title-edge), 0 2px 3px rgba(255,255,255,0.7);
    line-height: 0.95;
  }
  .title-line-small { display: block; font-size: 74px; letter-spacing: 1px; }
  .title-line-large { display: block; font-size: 118px; letter-spacing: 1px; margin-top: 4px; }
  .subtitle {
    position: absolute;
    right: 32px;
    top: 326px;
    text-align: left;
    font-size: 22px;
    font-weight: 500;
    line-height: 1.05;
    color: var(--subtitle-ink);
    letter-spacing: 0.3px;
  }
  .keywords {
    position: absolute;
    left: 42px;
    top: 692px;
    list-style: none;
    font-size: 19px;
    line-height: 34px;
    color: var(--keyword-ink);
    letter-spacing: 0.3px;
  }
  .byline {
    position: absolute;
    left: 42px;
    right: 20px;
    bottom: 38px;
    font-size: 27px;
    font-weight: 500;
    color: var(--byline-ink);
    letter-spacing: 0.2px;
    white-space: nowrap;
  }
  .symbol { position: absolute; }
  .symbol-star { right: 34px; top: 92px; width: 56px; height: 62px; }
  .symbol-crescent { right: 62px; top: 912px; width: 48px; height: 48px; }
</style>
</head>
<body>
  <main class="cover">
    <div class="cover-art" role="img" aria-label="Painted view of the US Capitol under a bright cloudy sky with trees on either side, reflected in a still pool"></div>

    <svg class="symbol symbol-star" viewBox="0 0 60 66" aria-hidden="true">
      <polygon points="30,2 56,48 4,48" fill="none" stroke="var(--symbol-ink)" stroke-width="3"/>
      <polygon points="30,64 56,18 4,18" fill="none" stroke="var(--symbol-ink)" stroke-width="3"/>
    </svg>

    <h1 class="title">
      <span class="title-line-small">WE WALK</span>
      <span class="title-line-large">BESIDE</span>
    </h1>

    <p class="subtitle">JEWISH &amp; MUSLIM<br>INTERFAITH DIALOGUE</p>

    <ul class="keywords">
      <li>RELIGION</li>
      <li>POLITICS</li>
      <li>PRESIDENT</li>
      <li>CALIFATE</li>
      <li>FREEDOM</li>
      <li>SHARIA LAW</li>
      <li>DEMOCRACY</li>
    </ul>

    <svg class="symbol symbol-crescent" viewBox="0 0 48 48" aria-hidden="true">
      <path d="M22 4 A20 20 0 1 0 40 36 A16 16 0 1 1 22 4 Z" fill="var(--symbol-ink)"/>
      <polygon points="36,14 38,20 44,20 39,24 41,30 36,26 31,30 33,24 28,20 34,20" fill="var(--symbol-ink)"/>
    </svg>

    <p class="byline">BY US NON-PROFIT VELMORA FOUNDATION</p>
  </main>
</body>
</html>
```